Meridale Cleaning Services

In need of a business card design suited for a growing cleaning company.

We offer our cleaning and maintenance services to a wide range of clients including but not limited to the following: constuction industry, hospitality, commercial, industrial and domestic

I want the card to be very noticable, i would like people to say 'hey, great card!' when i hand them my card.double sided would be nice

we want our business to come across as exceedingly professional and innovative (different).

a contemporary design is what we have in mind
we want to present an image of a quality business with a high standard of excellence in consistent service.

i just really need a card that persuades top end quality,
our business is very certified and also strives towards environmentaly friendly alternatives
Updates

hey sorry, i have uploaded my company logo design and name
cheers.

hey guys i have added my company logo/name file on my brief page. many thanks

sorry guys a typo in the brief..
address is Tolley Rd. not Tolly Rd
thanks

Industry/Entity Type

Industrial

Requirements
Must have
• company name: meridale cleaning services
operations manager: Colm Varetti
Tel: (02)9373 6204
Fax: (02)8645 7712
Mob: 0438571490

address: 47 Tolly RD Pymble NSW 2073
Postal Adress: PO Box 5832 North Ryde NSW 2113
email: meridaleclean@wexanet.com.au
website: meridalecleaningservices.com.au

```html
<!DOCTYPE html>
<html lang="en">
<head>
<meta charset="utf-8">
<title>Meridale Cleaning Services – Business Card</title>
<link rel="stylesheet" href="https://fonts.googleapis.com/css2?family=Arimo:wght@400;700&display=swap">
<style>
  :root {
    --stage: #5b5b5b;
    --card-blue: #1b80c8;
    --card-white: #ffffff;
    --brand-blue: #1a6db5;
    --brand-green: #4aa33c;
    --text-white: #ffffff;
    --text-grey: #7d7d7d;
    --rule-grey: #9a9a9a;
  }
  * { margin: 0; padding: 0; box-sizing: border-box; }
  html, body {
    width: 1200px;
    height: 900px;
    overflow: hidden;
    background: var(--stage);
    font-family: "Arimo", Arial, sans-serif;
  }
  .sheet {
    width: 1200px;
    height: 900px;
    display: flex;
    align-items: center;
    justify-content: center;
    gap: 44px;
  }
  .card {
    width: 520px;
    height: 300px;
    position: relative;
    flex: none;
  }

  /* Back side */
  .card--back { background: var(--card-blue); color: var(--text-white); }
  .card--back .brand-disc {
    position: absolute;
    left: 42px;
    top: 28px;
    width: 116px;
    height: 116px;
  }
  .contact {
    position: absolute;
    left: 40px;
    bottom: 44px;
    display: flex;
    align-items: stretch;
    font-size: 12px;
    line-height: 17px;
  }
  .contact__phones { padding-right: 10px; }
  .contact__rule { width: 1px; background: var(--text-white); }
  .contact__address { padding-left: 10px; }

  /* Front side */
  .card--front {
    background: var(--card-white);
    border: 2px solid #222;
  }
  .identity {
    position: absolute;
    left: 40px;
    top: 0;
    bottom: 0;
    display: flex;
    align-items: center;
  }
  .identity__mark {
    width: 38px;
    height: 38px;
    margin-right: 10px;
    flex: none;
  }
  .identity__name {
    font-weight: 700;
    font-size: 19px;
    line-height: 22px;
    color: var(--brand-blue);
    width: 132px;
  }
  .identity__rule {
    width: 1px;
    height: 40px;
    background: var(--rule-grey);
    margin: 0 10px 0 12px;
  }
  .person__name { font-size: 17px; color: var(--brand-blue); line-height: 20px; }
  .person__role { font-size: 13px; color: var(--text-grey); line-height: 16px; }
</style>
</head>
<body>
<main class="sheet">
  <section class="card card--back" aria-label="Business card back">
    <svg class="brand-disc" viewBox="0 0 100 100" aria-hidden="true">
      <circle cx="50" cy="50" r="50" fill="#2e9a5a"/>
    </svg>
    <div class="contact">
      <div class="contact__phones">
        <p>Tel: (02)9373 6204</p>
        <p>Fax: (02)8645 7712</p>
        <p>Mob: 0438571490</p>
      </div>
      <div class="contact__rule"></div>
      <div class="contact__address">
        <p>Address: 47 Tolley RD Pymble NSW 2073</p>
        <p>Postal Adress: PO Box 5832 North Ryde NSW 2113</p>
        <p>Email: meridaleclean@wexanet.com.au</p>
        <p>Website: meridalecleaningservices.com.au</p>
      </div>
    </div>
  </section>

  <section class="card card--front" aria-label="Business card front">
    <div class="identity">
      <svg class="identity__mark" viewBox="0 0 40 40" aria-hidden="true">
        <circle cx="20" cy="20" r="20" fill="#2e8fc0"/>
      </svg>
      <p class="identity__name">Meridale Cleaning Services</p>
      <div class="identity__rule"></div>
      <div class="person">
        <p class="person__name">Colm Varetti</p>
        <p class="person__role">operations manager</p>
      </div>
    </div>
  </section>
</main>
</body>
</html>
```